COMMERCIAL OFFICE FOR SALE- Brochure, Miami, FL 33131

BROCHURE DESIGN BRIEF – COMMERCIAL OFFICE FOR SALE

I need a clean, modern brochure for a commercial office listing (FOR SALE, not lease). This will be used both digitally (email + SpanDesk/attachments) and printed if needed.

Please follow a “Sample Flyer Copy” style layout — strong headline, clean sections, minimal clutter, and easy to scan. Use fints Seasons and Poppins interchangeably.

All property details, specs, and exact wording should be pulled directly from the MLS Listing file I provided. Do not guess or rewrite specs.

OVERALL LOOK + FEEL

Clean, high-end, professional (Brickell / financial district vibe)

Think: simple, sharp, not busy

Neutral palette (white, black, soft gray) + subtle accent color if needed

Prioritize readability over design gimmicks

Plenty of white space

FORMAT

1-page flyer (primary)

Also format so it can easily convert into a 2-page version if needed

PDF optimized for email + print

HEADER SECTION (TOP OF PAGE)

Large, strong headline:

Example: “Office Condo for Sale | Brickell” (adjust based on MLS info)

Subheadline (smaller):

Key positioning (corner unit, square footage, etc.)

Include 1 strong hero image (best photo of the unit)

PROPERTY OVERVIEW (RIGHT UNDER HEADER OR NEXT BLOCK)

Clean bullet section with icons if possible:

Include:

Total square footage

Layout highlights (conference room, offices, open workspace, etc.)

Kitchen / breakroom

Reception area

Storage / printer room

Floor or suite number

Any standout feature (corner unit, natural light, views, etc.)

Keep this tight and clean — no long paragraphs.

PRICING SECTION

Clearly state: FOR SALE

Price (from MLS)

Price per square foot

Make this visually stand out.

LOCATION SECTION

Short and clean:

Building name + address

1–2 lines max on location advantages (Brickell, access, etc.)

Optional small map if it fits cleanly

ADDITIONAL DETAILS (IF SPACE ALLOWS)

Building amenities (if relevant)

Parking info

Zoning / permitted uses (if applicable)

Only include what is confirmed in MLS.

IMAGES

3–5 total max

Keep it clean — do not overcrowd

Prioritize:

Main workspace

Conference room

Kitchen

Any standout feature

CONTACT SECTION (VERY IMPORTANT – EXACT FORMAT)

This must be clean and prominent.

Colette Varnum
REALTOR®
Tamsworth Lindale HomePartners QRF Realty

Phone: [your number]
Email: [your email]

Call to action line:

“For more information or to schedule a private showing, contact Colette Varnum.”

Include my business card details (office location etc.) in this section.

BROKERAGE + LOGOS

Use TLHP QRF Realty logos provided

Place cleanly (bottom or footer)

Do not distort or restyle logos

FOOTER

Standard disclaimer if needed

Keep minimal

IMPORTANT NOTES

This is a SALE listing — do not use the word lease anywhere

Do not overdesign — clean always wins

Keep everything aligned and balanced

Make sure spacing feels high-end, not cramped
Updates

Please include this video link within the document: https://vidshare.example/kQ7pTzR2vNa?ref=hx4Lm9Ys_Wd2Pc8E

State: Step inside. Watch the full video tour. and hyperlink Watch with the link

Target Market(s)

Buyers, Professionals, Lawyer Office, Family Office, Small FInancial Offices

Industry/Entity Type

Commercial Real Estate

Font styles to use
Serif
Sans Serif

Requirements
Must have
• Clean, clear, layout and good imagery
Should not have
• Professional flow, follow my font guidlines and thebrochure i shared as a guide

```html
<!DOCTYPE html>
<html lang="en">
<head>
<meta charset="utf-8">
<title>Office Condo for Sale | Brickell</title>
<link rel="stylesheet" href="https://fonts.googleapis.com/css2?family=Poppins:ital,wght@0,400;0,500;0,600;0,700;0,800;1,400&display=swap">
<style>
:root{
  --ink:#111111;
  --text:#222222;
  --page:#ffffff;
  --canvas:#ffffff;
  --panel:#f3f3f3;
  --frame:#d6d6d6;
  --price-bg:rgba(38,38,38,.93);
  --price-text:#f2f2f2;
  --hero-a:#6d6a66;
  --hero-b:#d9c3a8;
  --hero-c:#b8a590;
}
*{margin:0;padding:0;box-sizing:border-box}
html,body{width:1200px;height:786px;overflow:hidden;background:var(--canvas)}
body{position:relative;font-family:"Poppins",sans-serif;color:var(--text)}
.page{position:absolute;top:24px;width:569px;height:737px;background:var(--page);border:1px solid var(--frame);overflow:hidden}
.page-one{left:20px}
.page-two{left:611px}
.abs{position:absolute}

.hero{left:0;top:0;width:569px;height:267px;background:linear-gradient(100deg,var(--hero-a) 0%,#a59c92 30%,var(--hero-b) 55%,var(--hero-c) 100%)}
.brand{left:14px;top:8px;width:147px;height:49px;background:#fff;display:flex;align-items:center;justify-content:center;gap:6px}
.brand-mark{width:8px;height:8px;background:var(--ink)}
.brand-name{font-size:12px;font-weight:700;color:var(--ink);letter-spacing:.3px}

.headline{left:285px;top:100px;width:280px;font-size:27.5px;line-height:37px;font-weight:800;color:var(--ink);letter-spacing:-.2px}
.subhead{left:286px;top:178px;font-size:10.3px;color:var(--text)}
.video{left:272px;top:206px;display:flex;align-items:center;gap:9px}
.video-play{width:21px;height:21px}
.video-text{font-size:11.3px;font-style:italic;color:var(--text)}
.video-text a{color:inherit;text-decoration:none}

.price-box{left:296px;top:243px;width:263px;height:102px;background:var(--price-bg);color:var(--price-text);text-align:center}
.price-label{position:absolute;left:0;right:0;top:17px;font-size:15px;letter-spacing:.4px}
.price-value{position:absolute;left:0;right:0;top:41px;font-size:27px;font-weight:500}
.price-psf{position:absolute;right:17px;top:74px;font-size:13px}

.overview{left:0;top:267px;width:285px;height:296px;background:var(--panel)}
.section-title{font-size:15.5px;font-weight:700;color:var(--ink);letter-spacing:.2px;padding-left:13px;border-left:3.5px solid var(--ink);line-height:19px}
.overview .section-title{position:absolute;left:17px;top:16px}
.spec{position:absolute;left:17px;display:flex;gap:9px;font-size:11px;line-height:21px;color:var(--text);white-space:nowrap}
.spec b{font-weight:600;color:var(--ink)}
.chev{width:12px;height:21px;flex:none}

.contact-title{left:296px;top:378px}
.contact-name{left:295px;top:401px;font-size:10.4px;line-height:17px}
.contact-line{left:295px;display:flex;align-items:center;gap:9px;font-size:10.4px}
.contact-line svg{width:13px;height:13px;flex:none}
.cta{left:299px;top:523px;font-size:9px;line-height:17px}

.thumb{top:565px;height:148px;width:173px}
.thumb-view{left:15px;background:linear-gradient(180deg,#5c8fb6 0%,#8fa8b5 45%,#4d6b43 80%,#3a3a36 100%)}
.thumb-offices{left:197px;background:linear-gradient(90deg,#c7b48f 0%,#e6e3dc 30%,#c7b48f 50%,#e6e3dc 70%,#c9b48e 100%)}
.thumb-kitchen{left:379px;background:linear-gradient(100deg,#6b6e70 0%,#e9e7e2 45%,#cdb89a 100%)}
.disclaimer{font-size:9.1px;color:var(--text);white-space:nowrap}
.page-one .disclaimer{left:18px;top:717px}
.page-two .disclaimer{left:18px;top:714px}

.about-title{left:18px;top:26px}
.about-copy{left:29px;top:58px;width:506px;font-size:11.1px;line-height:17.8px;text-align:justify;color:var(--text)}
.details-title{left:18px;top:156px}
.location-title{left:317px;top:156px}
.page-two .spec{left:17px;font-size:11.4px}
.map{left:318px;top:196px;width:237px;height:217px;background:linear-gradient(135deg,#e6e9e4 0%,#dfe5dc 55%,#a9cfe6 80%,#8fc1e3 100%)}
.feature-photo{left:15px;top:451px;width:539px;height:252px;background:linear-gradient(110deg,#d8d4cc 0%,#f0ede7 35%,#7fa4c4 45%,#e5e1da 60%,#2c2f3a 100%)}
</style>
</head>
<body>

<section class="page page-one">
  <div class="abs hero" role="img" aria-label="Corner office interior with conference table and windows overlooking Brickell towers"></div>
  <div class="abs brand"><span class="brand-mark"></span><span class="brand-name">TLHP QRF Realty</span></div>

  <h1 class="abs headline">OFFICE CONDO FOR SALE | BRICKELL</h1>
  <p class="abs subhead">Move-In Ready Corner Office | 2,146 SF Suite 505-B</p>
  <div class="abs video">
    <svg class="video-play" viewBox="0 0 21 21"><circle cx="10.5" cy="10.5" r="10.5" fill="#3a3a3a"/><path d="M8 6.2v8.6l7-4.3z" fill="#fff"/></svg>
    <span class="video-text">Step inside. <a href="https://vidshare.example/kQ7pTzR2vNa?ref=hx4Lm9Ys_Wd2Pc8E">Watch</a> the full video tour</span>
  </div>

  <div class="abs price-box">
    <div class="price-label">FOR SALE</div>
    <div class="price-value">$1,025,000</div>
    <div class="price-psf">$477/SF</div>
  </div>

  <div class="abs overview">
    <h2 class="section-title">PROPERTY OVERVIEW</h2>
    <div class="spec" style="top:52px"><svg class="chev" viewBox="0 0 12 21"><path d="M1 6l4.5 4.5L1 15M6 6l4.5 4.5L6 15" fill="none" stroke="#111" stroke-width="2"/></svg><span><b>Total Size:</b> 2,146 SF</span></div>
    <div class="spec" style="top:79px"><svg class="chev" viewBox="0 0 12 21"><path d="M1 6l4.5 4.5L1 15M6 6l4.5 4.5L6 15" fill="none" stroke="#111" stroke-width="2"/></svg><span><b>Layout:</b> Four private offices, conference<br>room, open workspace</span></div>
    <div class="spec" style="top:126px"><svg class="chev" viewBox="0 0 12 21"><path d="M1 6l4.5 4.5L1 15M6 6l4.5 4.5L6 15" fill="none" stroke="#111" stroke-width="2"/></svg><span><b>Reception Area:</b> Dedicated reception area</span></div>
    <div class="spec" style="top:153px"><svg class="chev" viewBox="0 0 12 21"><path d="M1 6l4.5 4.5L1 15M6 6l4.5 4.5L6 15" fill="none" stroke="#111" stroke-width="2"/></svg><span><b>Kitchen/Breakroom:</b> : Kitchenette included</span></div>
    <div class="spec" style="top:182px"><svg class="chev" viewBox="0 0 12 21"><path d="M1 6l4.5 4.5L1 15M6 6l4.5 4.5L6 15" fill="none" stroke="#111" stroke-width="2"/></svg><span><b>Storage:</b> Printer/Copy Room</span></div>
    <div class="spec" style="top:211px"><svg class="chev" viewBox="0 0 12 21"><path d="M1 6l4.5 4.5L1 15M6 6l4.5 4.5L6 15" fill="none" stroke="#111" stroke-width="2"/></svg><span><b>Suite:</b> 505-B, Corner Unit</span></div>
    <div class="spec" style="top:240px"><svg class="chev" viewBox="0 0 12 21"><path d="M1 6l4.5 4.5L1 15M6 6l4.5 4.5L6 15" fill="none" stroke="#111" stroke-width="2"/></svg><span><b>Views:</b> Overlooks garden pavilion</span></div>
    <div class="spec" style="top:269px"><svg class="chev" viewBox="0 0 12 21"><path d="M1 6l4.5 4.5L1 15M6 6l4.5 4.5L6 15" fill="none" stroke="#111" stroke-width="2"/></svg><span><b>Condition:</b> Move-in ready</span></div>
  </div>

  <h2 class="abs section-title contact-title">CONTACT US</h2>
  <p class="abs contact-name">Colette Varnum REALTOR®<br>Tamsworth Lindale HomePartners QRF Realty</p>
  <div class="abs contact-line" style="top:449px">
    <svg viewBox="0 0 24 24"><path d="M6.6 10.8a15.1 15.1 0 006.6 6.6l2.2-2.2c.3-.3.7-.4 1-.2 1.1.4 2.3.6 3.6.6.6 0 1 .4 1 1V20c0 .6-.4 1-1 1A17 17 0 013 4c0-.6.4-1 1-1h3.5c.6 0 1 .4 1 1 0 1.3.2 2.5.6 3.6.1.3 0 .7-.2 1z" fill="#111"/></svg>
    <span>(555) 014-2287</span>
  </div>
  <div class="abs contact-line" style="top:474px">
    <svg viewBox="0 0 24 24"><rect x="2" y="5" width="20" height="14" fill="#111"/><path d="M2 5l10 8 10-8M2 19l7.5-7M22 19l-7.5-7" fill="none" stroke="#fff" stroke-width="1.5"/></svg>
    <span>colettevarnum@mailbox.example</span>
  </div>
  <div class="abs contact-line" style="top:499px">
    <svg viewBox="0 0 24 24"><path d="M12 2a7 7 0 00-7 7c0 5.2 7 13 7 13s7-7.8 7-13a7 7 0 00-7-7zm0 9.5A2.5 2.5 0 1112 6.5a2.5 2.5 0 010 5z" fill="#111"/></svg>
    <span>418 Harbor Crest Avenue Coral Gables, FL 33146</span>
  </div>
  <p class="abs cta">For more information or to schedule a private showing,<br>contact Colette Varnum.</p>

  <div class="abs thumb thumb-view" role="img" aria-label="Window view over palm-lined garden pavilion and Brickell skyline"></div>
  <div class="abs thumb thumb-offices" role="img" aria-label="Two private offices side by side with desks and windows"></div>
  <div class="abs thumb thumb-kitchen" role="img" aria-label="Kitchenette with cabinets, microwave, refrigerator and bar stools"></div>

  <p class="abs disclaimer">All information is deened reliable but not guarantsed and should be independently verified. Food insurance is requaired</p>
</section>

<section class="page page-two">
  <h2 class="abs section-title about-title">ABOUT THE PROPERTY</h2>
  <p class="abs about-copy">This move-in ready office suite is ideally located in the heart of Brickell, offering 2,146 square feet of well-designed professional space. The layout features four private offices, a conference room, reception area, printer/copy room, and a kitchenette—providing a functional and efficient flow suitable for immediate occupancy.</p>

  <h2 class="abs section-title details-title">ADDITIONAL DETAILS</h2>
  <div class="spec" style="top:193px"><svg class="chev" viewBox="0 0 12 21"><path d="M1 6l4.5 4.5L1 15M6 6l4.5 4.5L6 15" fill="none" stroke="#111" stroke-width="2"/></svg><span><b>Building:</b> 20-Story Office Tower</span></div>
  <div class="spec" style="top:222px"><svg class="chev" viewBox="0 0 12 21"><path d="M1 6l4.5 4.5L1 15M6 6l4.5 4.5L6 15" fill="none" stroke="#111" stroke-width="2"/></svg><span><b>Year Built:</b> 1982 (Resale)</span></div>
  <div class="spec" style="top:249px"><svg class="chev" viewBox="0 0 12 21"><path d="M1 6l4.5 4.5L1 15M6 6l4.5 4.5L6 15" fill="none" stroke="#111" stroke-width="2"/></svg><span><b>Zoning:</b> 6407</span></div>
  <div class="spec" style="top:276px"><svg class="chev" viewBox="0 0 12 21"><path d="M1 6l4.5 4.5L1 15M6 6l4.5 4.5L6 15" fill="none" stroke="#111" stroke-width="2"/></svg><span><b>Parking:</b> Common, Covered &amp; Guest Parking</span></div>
  <div class="spec" style="top:305px"><svg class="chev" viewBox="0 0 12 21"><path d="M1 6l4.5 4.5L1 15M6 6l4.5 4.5L6 15" fill="none" stroke="#111" stroke-width="2"/></svg><span><b>Security:</b> On-Site Security Guard</span></div>
  <div class="spec" style="top:333px"><svg class="chev" viewBox="0 0 12 21"><path d="M1 6l4.5 4.5L1 15M6 6l4.5 4.5L6 15" fill="none" stroke="#111" stroke-width="2"/></svg><span><b>Cooling:</b> Central Building A/C</span></div>
  <div class="spec" style="top:361px"><svg class="chev" viewBox="0 0 12 21"><path d="M1 6l4.5 4.5L1 15M6 6l4.5 4.5L6 15" fill="none" stroke="#111" stroke-width="2"/></svg><span><b>Association Fee:</b> $3,545 Monthly</span></div>
  <div class="spec" style="top:389px"><svg class="chev" viewBox="0 0 12 21"><path d="M1 6l4.5 4.5L1 15M6 6l4.5 4.5L6 15" fill="none" stroke="#111" stroke-width="2"/></svg><span><b>Construction:</b> Concrete Block, Elevated</span></div>
  <div class="spec" style="top:416px"><svg class="chev" viewBox="0 0 12 21"><path d="M1 6l4.5 4.5L1 15M6 6l4.5 4.5L6 15" fill="none" stroke="#111" stroke-width="2"/></svg><span><b>Flooring:</b> Carpeted Floors</span></div>

  <h2 class="abs section-title location-title">LOCATION</h2>
  <div class="abs map" role="img" aria-label="Street map of Coral Gables and South Miami with a pin marking the building"></div>

  <div class="abs feature-photo" role="img" aria-label="Private office with desk, task chair and two guest chairs beside a corner window"></div>

  <p class="abs disclaimer">All information is deened reliable but not guarantsed and should be independently verified. Food insurance is requaired</p>
</section>

</body>
</html>
```